Brightmoor Towing Website

New Pittsburgh, PA towing company looking for a unique and easy to use website with a professional look. We would like the customer to feel confident when booking with us. We offer reliable services with no hidden fees or predatory towing tactics. Designs that incorporate our logo & color scheme are preferred. Looking for websites designed similar to https://calverlyhaulservice.com/

```html
<!DOCTYPE html>
<html lang="en">
<head>
<meta charset="utf-8">
<title>Brightmoor Towing</title>
<link href="https://fonts.googleapis.com/css2?family=Montserrat:wght@400;500;600;700&display=swap" rel="stylesheet">
<style>
:root{
  --maroon:#5e1313;
  --gold:#d1a32f;
  --gold-dark:#b8902a;
  --ink:#111;
  --body:#2b2b2b;
  --header:#1a1412;
  --cream:#f8efdb;
  --contact:#121010;
  --white:#fff;
}
*{margin:0;padding:0;box-sizing:border-box}
html,body{width:1200px;height:3271px;overflow:hidden}
body{position:relative;font-family:'Montserrat',sans-serif;color:var(--body);background:var(--white)}
.abs{position:absolute}
.btn{position:absolute;background:var(--maroon);color:var(--white);font-size:16px;font-weight:500;display:flex;align-items:center;justify-content:center;border-radius:2px}
.photo{position:absolute}
/* header */
.site-header{left:0;top:0;width:1200px;height:155px;background:var(--header)}
.brand{left:95px;top:55px;display:flex;align-items:center;gap:12px;color:var(--gold);font-size:30px;font-weight:500;letter-spacing:1px}
.brand-dot{width:16px;height:16px;border-radius:50%;background:var(--gold)}
.header-phone{left:712px;top:46px;color:var(--gold);font-size:17px;font-weight:600;display:flex;align-items:center;gap:14px}
.header-btn{left:894px;top:40px;width:194px;height:36px;background:var(--gold);color:var(--header);font-size:15px;font-weight:500;display:flex;align-items:center;justify-content:center}
.main-nav{right:112px;top:107px;display:flex;gap:25px;font-size:14px;color:var(--white)}
.main-nav .active{color:var(--gold)}
/* hero */
.hero{left:0;top:155px;width:1200px;height:512px;background:var(--cream)}
.hero-title{left:714px;top:282px;font-size:53px;color:var(--maroon);font-weight:400;letter-spacing:1px}
.hero-sub{left:715px;top:350px;font-size:24px;letter-spacing:6px;color:#333}
.hero-btn{left:717px;top:396px;width:253px;height:40px;font-size:14px;letter-spacing:3px;gap:14px}
.gold-rule{left:0;top:666px;width:1200px;height:9px;background:var(--gold)}
.features{left:112px;top:576px;width:976px;height:161px;background:var(--maroon);border-top:8px solid var(--gold);display:flex;align-items:center;justify-content:space-around;padding:0 30px}
.feature{display:flex;align-items:center;gap:20px;color:var(--white);font-weight:600;font-size:17px;line-height:25px}
/* content */
h2{position:absolute;font-size:36px;font-weight:500;color:var(--ink);line-height:50px}
h2 span{color:var(--gold)}
.copy{position:absolute;font-size:14.5px;line-height:24px;color:var(--body)}
.ticks{left:645px;top:1440px;list-style:none;font-size:14.5px;color:var(--maroon)}
.ticks li{display:flex;align-items:center;gap:17px;height:27.3px}
.tick{width:13px;height:13px;background:var(--maroon);display:flex;align-items:center;justify-content:center}
/* testimonial */
.testimonial{left:0;top:1760px;width:1200px;height:442px;background:linear-gradient(180deg,#1b2438 0%,#141c2c 60%,#2a2119 85%,#151210 100%)}
.quote-text{left:426px;top:1898px;width:648px;font-size:13.5px;line-height:22.5px;color:#e8e8e8}
.quote-name{left:426px;top:2034px;font-size:22px;color:var(--white)}
/* contact */
.contact{left:0;top:2745px;width:1200px;height:526px;background:var(--contact)}
.contact-title{left:112px;top:2785px;font-size:48px;font-weight:600;color:var(--gold)}
.contact-lead{left:113px;top:2860px;width:470px;font-size:17px;font-weight:600;line-height:28px;color:var(--white)}
.info{left:113px;color:var(--white);font-size:12.5px;line-height:23px}
.info h4{display:flex;align-items:center;gap:14px;color:var(--gold);font-size:16.5px;font-weight:500;margin-bottom:4px}
.info p{padding-left:33px}
.divider{left:407px;top:2940px;width:1px;height:255px;background:var(--maroon)}
.quick{left:469px;top:2955px;color:var(--white);font-size:12.5px;line-height:25.7px}
.quick h4{color:var(--gold);font-size:16.5px;font-weight:500;margin-bottom:6px}
.form-title{left:627px;top:2802px;font-size:25px;font-weight:600;line-height:36px;color:var(--gold)}
.field{position:absolute;background:var(--white);border:1px solid #ccc;font-size:12.5px;color:#666;padding:0 20px;display:flex;align-items:center;justify-content:space-between}
.submit{left:923px;top:3130px;width:158px;height:38px;font-size:14px;letter-spacing:3px}
.footer-line{left:112px;top:3210px;width:976px;height:1px;background:var(--gold-dark)}
.social{left:112px;top:3229px;display:flex;gap:10px}
.social span{width:25px;height:25px;border-radius:50%;background:#3b6fb6}
.copyright{right:112px;top:3232px;color:var(--white);font-size:13.5px}
.code{left:1142px;top:3232px;color:var(--white);font-size:13.5px}
</style>
</head>
<body>
<header class="abs site-header">
  <div class="abs brand"><i class="brand-dot"></i>Brightmoor</div>
  <div class="abs header-phone">
    <svg width="18" height="18" viewBox="0 0 24 24"><path fill="#d1a32f" d="M6.6 10.8a15.2 15.2 0 0 0 6.6 6.6l2.2-2.2c.3-.3.7-.4 1-.2 1.1.4 2.3.6 3.6.6.6 0 1 .4 1 1V20c0 .6-.4 1-1 1A17 17 0 0 1 3 4c0-.6.4-1 1-1h3.5c.6 0 1 .4 1 1 0 1.3.2 2.5.6 3.6.1.3 0 .7-.2 1z"/></svg>412-555-0186</div>
  <div class="abs header-btn">APPOINTMENTS</div>
  <nav class="abs main-nav"><span class="active">HOME</span><span>SERVICES</span><span>REVIEWS</span><span>AREAS</span><span>IMPOUNDS</span><span>ABOUT</span><span>CONTACT</span></nav>
</header>

<section class="abs hero"></section>
<div class="photo" role="img" aria-label="Yellow flatbed tow truck carrying a damaged dark car" style="left:50px;top:195px;width:650px;height:325px;background:linear-gradient(135deg,#e7c64a 0%,#c9a52a 55%,#4a4a4a 100%);border-radius:4px"></div>
<h1 class="abs hero-title">BRIGHTMOOR</h1>
<div class="abs hero-sub">PA TOWING COMPANY.</div>
<div class="btn hero-btn">SCHEDULE SERVICE <svg width="12" height="10" viewBox="0 0 12 10"><path d="M0 5h9M6 1l4 4-4 4" stroke="#fff" stroke-width="2" fill="none"/></svg></div>

<div class="abs gold-rule"></div>
<div class="abs features">
  <div class="feature">
    <svg width="84" height="76" viewBox="0 0 84 76" fill="#fff"><circle cx="16" cy="14" r="6"/><circle cx="42" cy="8" r="6"/><circle cx="64" cy="18" r="5"/><rect x="10" y="22" width="12" height="30" rx="3"/><rect x="35" y="16" width="14" height="34" rx="3"/><rect x="58" y="26" width="12" height="24" rx="3"/><rect x="11" y="50" width="4" height="22"/><rect x="17" y="50" width="4" height="22"/><rect x="37" y="48" width="4" height="24"/><rect x="43" y="48" width="4" height="24"/><rect x="60" y="48" width="3" height="22"/><rect x="65" y="48" width="3" height="22"/></svg>
    <div>FAMILY OWNED<br>&amp; OPERATED</div></div>
  <div class="feature">
    <svg width="72" height="62" viewBox="0 0 72 62" fill="none" stroke="#fff" stroke-width="5"><path d="M8 4l24 34"/><path d="M32 38h14V24h12l10 14v8H4v-8h28z" fill="#fff"/><circle cx="18" cy="52" r="6" fill="#5e1313"/><circle cx="56" cy="52" r="6" fill="#5e1313"/></svg>
    <div>ROADSIDE<br>ASSISTANCE</div></div>
  <div class="feature">
    <svg width="78" height="78" viewBox="0 0 78 78"><circle cx="40" cy="38" r="32" fill="none" stroke="#fff" stroke-width="5"/><text x="40" y="47" text-anchor="middle" fill="#fff" font-family="Montserrat,sans-serif" font-weight="700" font-size="25">24</text></svg>
    <div>24 HOUR<br>EMERGENCY SERVICE</div></div>
</div>

<h2 style="left:112px;top:798px">About <span>Brightmoor</span></h2>
<p class="copy" style="left:112px;top:853px;width:448px">Sed ut perspiciatis unde omnis iste natus error sit voluptatem accusantium doloremque laudantium, totam rem aperiam, eaque ipsa quae ab illo inventore veritatis et quasi architecto beatae vitae dicta sunt explicabo. Nemo enim ipsam voluptatem quia voluptas sit aspernatur aut odit aut fugit, sed quia consequuntur magni dolores eos qui ratione voluptatem sequi nesciunt.</p>
<p class="copy" style="left:112px;top:1044px;width:440px">Neque porro quisquam est, qui dolorem ipsum quia dolor sit amet, consectetur, adipisci velit, sed quia non numquam eius modi tempora incidunt ut labore et dolore magnam aliquam quaerat voluptatem.</p>
<div class="btn" style="left:112px;top:1153px;width:195px;height:37px">READ MORE ABOUT</div>
<div class="photo" role="img" aria-label="Tow operator in a yellow high-visibility jacket writing on a clipboard" style="left:600px;top:811px;width:487px;height:379px;background:linear-gradient(135deg,#e6d9d0 0%,#d9c24a 50%,#a05060 100%)"></div>

<h2 style="left:645px;top:1262px">Brightmoor <span>Services</span></h2>
<p class="copy" style="left:645px;top:1317px;width:430px">Sed ut perspiciatis unde omnis iste natus error sit voluptatem accusantium doloremque laudantium, totam rem aperiam, eaque ipsa quae ab illo inventore veritatis et quasi architecto beatae vitae dicta sunt explicabo.</p>
<ul class="abs ticks">
  <li><i class="tick"><svg width="9" height="8" viewBox="0 0 9 8"><path d="M1 4l2.5 2.5L8 1" stroke="#fff" stroke-width="1.8" fill="none"/></svg></i>Sed ut perspiciatis unde</li>
  <li><i class="tick"><svg width="9" height="8" viewBox="0 0 9 8"><path d="M1 4l2.5 2.5L8 1" stroke="#fff" stroke-width="1.8" fill="none"/></svg></i>Unde omnis iste natus error sit</li>
  <li><i class="tick"><svg width="9" height="8" viewBox="0 0 9 8"><path d="M1 4l2.5 2.5L8 1" stroke="#fff" stroke-width="1.8" fill="none"/></svg></i>Sed ut perspiciatis unde omnis</li>
  <li><i class="tick"><svg width="9" height="8" viewBox="0 0 9 8"><path d="M1 4l2.5 2.5L8 1" stroke="#fff" stroke-width="1.8" fill="none"/></svg></i>Perspiciatis unde omnis iste natus erro</li>
  <li><i class="tick"><svg width="9" height="8" viewBox="0 0 9 8"><path d="M1 4l2.5 2.5L8 1" stroke="#fff" stroke-width="1.8" fill="none"/></svg></i>Omnis iste natus error sit</li>
  <li><i class="tick"><svg width="9" height="8" viewBox="0 0 9 8"><path d="M1 4l2.5 2.5L8 1" stroke="#fff" stroke-width="1.8" fill="none"/></svg></i>Sed ut perspiciatis unde omnis iste natus error sit</li>
  <li><i class="tick"><svg width="9" height="8" viewBox="0 0 9 8"><path d="M1 4l2.5 2.5L8 1" stroke="#fff" stroke-width="1.8" fill="none"/></svg></i>Sed ut perspiciatis</li>
</ul>
<div class="btn" style="left:645px;top:1648px;width:195px;height:37px">APPOINTMENTS</div>
<div class="photo" role="img" aria-label="Black flatbed tow truck with striped bed" style="left:80px;top:1365px;width:490px;height:255px;background:linear-gradient(135deg,#8a8a8a 0%,#3a3a3a 60%,#c9a52a 100%);border-radius:6px"></div>

<section class="abs testimonial" role="img" aria-label="Night roadside scene with a broken-down car at sunset"></section>
<div class="photo" role="img" aria-label="Customer portrait" style="left:73px;top:1793px;width:250px;height:250px;border-radius:50%;background:radial-gradient(circle at 45% 40%,#d9c9a8,#7a2a2a 70%,#2a2a2a)"></div>
<svg class="abs" style="left:165px;top:2030px" width="64" height="52" viewBox="0 0 64 52"><path fill="#e0b63a" d="M2 30c0-16 8-26 22-30l2 6C17 10 13 16 13 22h13v28H2zM36 30c0-16 8-26 22-30l2 6c-9 4-13 10-13 16h13v28H36z"/></svg>
<svg class="abs" style="left:426px;top:1843px" width="188" height="36" viewBox="0 0 188 36"><g fill="#f0b820"><polygon id="st" points="18,1 22.5,13 35,13 25,21 29,34 18,26 7,34 11,21 1,13 13.5,13"/><use href="#st" x="38"/><use href="#st" x="76"/><use href="#st" x="114"/><use href="#st" x="152"/></g></svg>
<p class="abs quote-text">“Lorem Ipsum is simply dummy text of the printing and typesetting industry. Lorem Ipsum has been the industry's standard dummy text ever since the 1500s, when an unknown printer took a galley of type and scrambled it to make a type specimen book. It has survived not only five centuries, but also the leap into electronic typesetting, remaining essentially unchanged. It was popularised in the 1960s with the release of Letraset sheets containing”</p>
<div class="abs quote-name">-&nbsp;&nbsp;&nbsp;&nbsp;Dana M Hollis</div>
<svg class="abs" style="left:561px;top:2107px" width="80" height="34" viewBox="0 0 80 34"><circle cx="17" cy="17" r="15.5" fill="none" stroke="#e0b63a" stroke-width="2"/><path d="M20 11l-6 6 6 6" stroke="#e0b63a" stroke-width="2" fill="none"/><circle cx="60" cy="17" r="17" fill="#e0b63a"/><path d="M57 11l6 6-6 6" stroke="#fff" stroke-width="2" fill="none"/></svg>

<h2 style="left:112px;top:2265px">Dedicated to<br><span>Customer Service</span></h2>
<p class="copy" style="left:112px;top:2373px;width:440px">Sed ut perspiciatis unde omnis iste natus error sit voluptatem accusantium doloremque laudantium, totam rem aperiam, eaque ipsa quae ab illo inventore veritatis et quasi architecto beatae vitae dicta sunt explicabo. nesciunt.</p>
<p class="copy" style="left:112px;top:2492px;width:440px">Neque porro quisquam est, qui dolorem ipsum quia dolor sit amet, consectetur, adipisci velit, sed quia non numquam eius modi tempora incidunt ut labore et dolore magnam aliquam quaerat voluptatem.</p>
<div class="btn" style="left:112px;top:2620px;width:195px;height:37px">CALL US SERVICES</div>
<div class="photo" role="img" aria-label="Damaged red car loaded onto a flatbed tow truck in front of green trees" style="left:600px;top:2279px;width:487px;height:379px;background:linear-gradient(160deg,#4f7a33 0%,#3b5f28 45%,#b3303a 70%,#4a4a48 100%)"></div>

<section class="abs contact"></section>
<div class="abs contact-title">Contact Us</div>
<p class="abs contact-lead">Neque porro quisquam est qui dolorem ipsum quia dolor sit amet, consectetur, adipisci velit...</p>
<div class="abs info" style="top:2944px">
  <h4><svg width="14" height="18" viewBox="0 0 14 18"><path fill="#d1a32f" d="M7 0a7 7 0 0 0-7 7c0 5 7 11 7 11s7-6 7-11a7 7 0 0 0-7-7zm0 10a3 3 0 1 1 0-6 3 3 0 0 1 0 6z"/></svg>Brightmoor</h4>
  <p>2270 Harlow Avenue, Millvale,<br>Pennsylvania, 15209.</p>
</div>
<div class="abs info" style="top:3036px">
  <h4><svg width="16" height="16" viewBox="0 0 24 24"><path fill="#d1a32f" d="M6.6 10.8a15.2 15.2 0 0 0 6.6 6.6l2.2-2.2c.3-.3.7-.4 1-.2 1.1.4 2.3.6 3.6.6.6 0 1 .4 1 1V20c0 .6-.4 1-1 1A17 17 0 0 1 3 4c0-.6.4-1 1-1h3.5c.6 0 1 .4 1 1 0 1.3.2 2.5.6 3.6.1.3 0 .7-.2 1z"/></svg>Phone</h4>
  <p>412-555-0186</p>
</div>
<div class="abs info" style="top:3100px">
  <h4><svg width="16" height="12" viewBox="0 0 16 12"><rect width="16" height="12" fill="#d1a32f"/><path d="M0 0l8 6 8-6" stroke="#121010" fill="none"/></svg>Email</h4>
  <p>info@brightmoortowing.com</p>
</div>
<div class="abs divider"></div>
<div class="abs quick">
  <h4>Quick Links</h4>
  HOME<br>SERVICES<br>REVIEWS<br>APPOINTMENTS<br>AREAS<br>IMPOUNDS<br>ABOUT<br>CONTACT
</div>
<div class="abs form-title">Feel confident when<br>booking with us.</div>
<div class="field" style="left:622px;top:2898px;width:226px;height:33px">First Name</div>
<div class="field" style="left:856px;top:2898px;width:226px;height:33px">Laste Name</div>
<div class="field" style="left:622px;top:2938px;width:226px;height:33px">Phone</div>
<div class="field" style="left:856px;top:2938px;width:226px;height:33px">Email</div>
<div class="field" style="left:622px;top:2978px;width:226px;height:33px">Select Your Services <svg width="8" height="5"><path d="M0 0h8L4 5z" fill="#333"/></svg></div>
<div class="field" style="left:856px;top:2978px;width:226px;height:33px">Select Address <svg width="8" height="5"><path d="M0 0h8L4 5z" fill="#333"/></svg></div>
<div class="field" style="left:622px;top:3018px;width:460px;height:98px;align-items:flex-start;padding-top:12px">Message here...</div>
<div class="btn submit">SUBMIT NOW</div>
<div class="abs footer-line"></div>
<div class="abs social"><span></span><span></span><span></span><span></span><span></span></div>
<div class="abs copyright">Brightmoor.&nbsp; © 2021. All rights reserved.</div>
<div class="abs code">C24</div>
</body>
</html>
```